Bold and Enticing Product Packaging - Dog Rolls (wet pet food)

Hello there and welcome to our project! Looking for fun and creative designs for our Dog Rolls (Wet Pet Food Rolls) sold at our butchery retail store.

We are a business located in Papua New Guinea and we manufacture and produce goods that we retail. Our target audience responds better to graphics/visual images rather than reading information - so keep it simple and attractive! Most animals here are working dogs (not leisure pets), so we must focus on this e.g. sell as ‘power for your dog’.

Looking for 2 x designs for each size (1kg & 3kg) – can be the same with different colour schemes/formats or similar. Require to be fully editable in both AI/PSD format.

Packaging dimensions are below. Designs will need to be repeated to fill 1m plastic casing. Note - more colours, more money, keep the colours to a minimum.
1kg product - 1 roll is 11cm wide (length of roll) and 25cm long (wrapped around). 1cm bleed.
3kg product - 1 roll is 16cm wide and 36cm long. 1cm bleed.

Information required (must have):
• 1kg or 3kg
• Real photo of a WORKING DOG (e.g. bullmastiff, doberman, rottweiler, german sheppard) and pet dog
• Brava Tusk logo & “power for your dog” combined... to read “Brava Tusk Power For Your Dog”.
• “Complete nutrition – for all dogs big or small”
• “Pet food only, not for human consumption. Keep refrigerated”

Would be cool (not a must-have) if we could include and be able to interchange the title of flavours (different products) e.g. Original Chunky.

Thank you and look forward to collaborating on some great designs here :)

Target Market(s)

See brief

Font styles to use
Sans Serif

Requirements
Must have
• See brief

```html
<!DOCTYPE html>
<html lang="en">
<head>
<meta charset="utf-8">
<title>Brava Tusk Dog Roll Labels</title>
<link rel="stylesheet" href="https://fonts.googleapis.com/css2?family=Oswald:wght@400;600;700&family=Cinzel:wght@700&family=Playfair+Display:wght@700&family=PT+Serif&display=swap">
<style>
  :root {
    --bg-top: #4a4a4a;
    --bg-mid: #e9e9e9;
    --bg-low: #9a9a9a;
    --beef: #f39e6d;
    --chunky: #37b6f6;
    --brand-red: #b3121a;
    --title-red: #c8141b;
    --ink: #111111;
    --white: #ffffff;
    --unit-h: 238.4px;
  }
  * { box-sizing: border-box; margin: 0; padding: 0; }
  html, body { width: 853px; height: 1200px; overflow: hidden; }
  body {
    background: linear-gradient(180deg, var(--bg-top) 0%, #8a8a8a 30%, var(--bg-mid) 62%, var(--bg-low) 100%);
    position: relative;
    font-family: "Oswald", sans-serif;
  }
  .label-sheet {
    position: absolute;
    top: 62px;
    width: 353px;
    height: 732px;
    overflow: hidden;
  }
  .label-sheet--beef { left: 58px; background: var(--beef); }
  .label-sheet--chunky { left: 442px; background: var(--chunky); }

  .cut-frame {
    position: absolute;
    left: 16px; top: 14px;
    width: 318px; height: 702px;
    border: 1px dashed rgba(255,255,255,0.8);
  }

  .label-unit {
    position: absolute;
    left: 0; width: 353px; height: var(--unit-h);
  }
  .label-unit:nth-of-type(1) { top: 0; }
  .label-unit:nth-of-type(2) { top: 238.4px; }
  .label-unit:nth-of-type(3) { top: 476.8px; }

  .dog-photo {
    position: absolute;
    left: 68px; top: 17px;
    width: 134px; height: 128px;
    border-radius: 46% 46% 10% 30%;
    background: radial-gradient(ellipse at 60% 40%, #3a2e28 0%, #1a1614 55%, rgba(26,22,20,0) 78%);
  }

  .partner-mark {
    position: absolute;
    left: 25px; top: 63px;
    width: 42px; height: 42px;
    border-radius: 50%;
    background: var(--white);
    border: 2px solid var(--ink);
    display: flex; align-items: center; justify-content: center;
    text-align: center;
    font-size: 7px; line-height: 1.05; font-weight: 600;
    color: var(--brand-red);
  }

  .brand-lockup {
    position: absolute;
    left: 26px; top: 146px;
    width: 200px;
    text-align: center;
  }
  .brand-name {
    font-family: "Cinzel", serif;
    font-weight: 700;
    font-size: 27px;
    line-height: 1;
    color: var(--brand-red);
    white-space: nowrap;
  }
  .brand-tagline {
    font-family: "PT Serif", serif;
    font-size: 12px;
    letter-spacing: 1px;
    color: var(--ink);
    margin-top: 8px;
    white-space: nowrap;
    transform: rotate(3deg);
  }

  .bone-tag {
    position: absolute;
    left: 232px; top: 36px;
    width: 84px; height: 33px;
  }
  .bone-tag svg { position: absolute; inset: 0; }
  .bone-tag span {
    position: relative;
    display: block;
    text-align: center;
    line-height: 33px;
    color: var(--white);
    font-weight: 600;
    font-size: 15px;
  }

  .nutrition-claim {
    position: absolute;
    left: 232px; top: 89px;
    width: 90px;
    text-align: center;
    color: var(--white);
    font-weight: 700;
    font-size: 16px;
    line-height: 15px;
  }
  .nutrition-claim small {
    display: block;
    font-weight: 400;
    font-size: 7px;
    line-height: 10px;
    color: var(--title-red);
    margin-top: 2px;
  }

  .storage-note {
    position: absolute;
    left: 234px; top: 149px;
    width: 100px;
    text-align: center;
    color: var(--ink);
    font-size: 7px;
    line-height: 10px;
    white-space: nowrap;
  }

  .flavour-band {
    position: absolute;
    left: 0; top: 208px;
    width: 353px; height: 23.5px;
    background: var(--white);
  }
  .flavour-title {
    position: absolute;
    left: 26px; width: 200px;
    top: 0; line-height: 24px;
    text-align: center;
    font-family: "Playfair Display", serif;
    font-weight: 700;
    font-size: 20px;
    color: var(--title-red);
    white-space: nowrap;
    transform: scaleX(0.86);
  }
  .net-weight {
    position: absolute;
    left: 244px; top: 2px;
    width: 70px;
    text-align: center;
    font-size: 6px; line-height: 8px;
    color: var(--ink);
  }
  .net-weight b { display: block; font-size: 9px; font-weight: 600; line-height: 10px; }

  .fortified-note {
    position: absolute;
    left: 26px; top: 234px;
    width: 204px;
    text-align: center;
    font-family: "PT Serif", serif;
    font-size: 7.5px;
    color: var(--ink);
    white-space: nowrap;
  }
</style>
</head>
<body>

<svg width="0" height="0" style="position:absolute">
  <defs>
    <path id="bone-shape" d="M10 2 a8 8 0 0 1 10 6 H64 a8 8 0 0 1 10 -6 a8 8 0 0 1 6 10 a6 6 0 0 1 0 9 a8 8 0 0 1 -6 10 a8 8 0 0 1 -10 -6 H20 a8 8 0 0 1 -10 6 a8 8 0 0 1 -6 -10 a6 6 0 0 1 0 -9 a8 8 0 0 1 6 -10 z"/>
  </defs>
</svg>

<section class="label-sheet label-sheet--beef" aria-label="Beef Formula 1kg roll label">
  <div class="cut-frame"></div>

  <article class="label-unit">
    <div class="dog-photo" role="img" aria-label="Photo of a black, tan and white mountain dog, mouth open"></div>
    <div class="partner-mark">KUMUL<br>PETS</div>
    <div class="brand-lockup"><div class="brand-name">Brava Tusk</div><div class="brand-tagline">POWER FOR YOUR DOG</div></div>
    <div class="bone-tag"><svg viewBox="0 0 84 33"><use href="#bone-shape" fill="#111"/></svg><span>DOG FOOD</span></div>
    <div class="nutrition-claim">COMPLETE<br>NUTRITION<small>for all dogs big or small</small></div>
    <div class="storage-note">PET FOOD ONLY,<br>NOT FOR HUMAN CONSUMPTION.<br>KEEP REFRIGERATED</div>
    <div class="flavour-band"><div class="flavour-title">BEEF FORMULA</div><div class="net-weight">Net weight:<b>1kg (35.27)</b></div></div>
    <div class="fortified-note">*with added vitamins, minerals and other nutrients</div>
  </article>

  <article class="label-unit">
    <div class="dog-photo" role="img" aria-label="Photo of a black, tan and white mountain dog, mouth open"></div>
    <div class="partner-mark">KUMUL<br>PETS</div>
    <div class="brand-lockup"><div class="brand-name">Brava Tusk</div><div class="brand-tagline">POWER FOR YOUR DOG</div></div>
    <div class="bone-tag"><svg viewBox="0 0 84 33"><use href="#bone-shape" fill="#111"/></svg><span>DOG FOOD</span></div>
    <div class="nutrition-claim">COMPLETE<br>NUTRITION<small>for all dogs big or small</small></div>
    <div class="storage-note">PET FOOD ONLY,<br>NOT FOR HUMAN CONSUMPTION.<br>KEEP REFRIGERATED</div>
    <div class="flavour-band"><div class="flavour-title">BEEF FORMULA</div><div class="net-weight">Net weight:<b>1kg (35.27)</b></div></div>
    <div class="fortified-note">*with added vitamins, minerals and other nutrients</div>
  </article>

  <article class="label-unit">
    <div class="dog-photo" role="img" aria-label="Photo of a black, tan and white mountain dog, mouth open"></div>
    <div class="partner-mark">KUMUL<br>PETS</div>
    <div class="brand-lockup"><div class="brand-name">Brava Tusk</div><div class="brand-tagline">POWER FOR YOUR DOG</div></div>
    <div class="bone-tag"><svg viewBox="0 0 84 33"><use href="#bone-shape" fill="#111"/></svg><span>DOG FOOD</span></div>
    <div class="nutrition-claim">COMPLETE<br>NUTRITION<small>for all dogs big or small</small></div>
    <div class="storage-note">PET FOOD ONLY,<br>NOT FOR HUMAN CONSUMPTION.<br>KEEP REFRIGERATED</div>
    <div class="flavour-band"><div class="flavour-title">BEEF FORMULA</div><div class="net-weight">Net weight:<b>1kg (35.27)</b></div></div>
    <div class="fortified-note">*with added vitamins, minerals and other nutrients</div>
  </article>
</section>

<section class="label-sheet label-sheet--chunky" aria-label="Original Chunky 1kg roll label">
  <div class="cut-frame"></div>

  <article class="label-unit">
    <div class="dog-photo" role="img" aria-label="Photo of a black, tan and white mountain dog, mouth open"></div>
    <div class="partner-mark">KUMUL<br>PETS</div>
    <div class="brand-lockup"><div class="brand-name">Brava Tusk</div><div class="brand-tagline">POWER FOR YOUR DOG</div></div>
    <div class="bone-tag"><svg viewBox="0 0 84 33"><use href="#bone-shape" fill="#111"/></svg><span>DOG FOOD</span></div>
    <div class="nutrition-claim">COMPLETE<br>NUTRITION<small>for all dogs big or small</small></div>
    <div class="storage-note">PET FOOD ONLY,<br>NOT FOR HUMAN CONSUMPTION.<br>KEEP REFRIGERATED</div>
    <div class="flavour-band"><div class="flavour-title">ORIGINAL CHUNKY</div><div class="net-weight">Net weight:<b>1kg (35.27)</b></div></div>
    <div class="fortified-note">*with added vitamins, minerals and other nutrients</div>
  </article>

  <article class="label-unit">
    <div class="dog-photo" role="img" aria-label="Photo of a black, tan and white mountain dog, mouth open"></div>
    <div class="partner-mark">KUMUL<br>PETS</div>
    <div class="brand-lockup"><div class="brand-name">Brava Tusk</div><div class="brand-tagline">POWER FOR YOUR DOG</div></div>
    <div class="bone-tag"><svg viewBox="0 0 84 33"><use href="#bone-shape" fill="#111"/></svg><span>DOG FOOD</span></div>
    <div class="nutrition-claim">COMPLETE<br>NUTRITION<small>for all dogs big or small</small></div>
    <div class="storage-note">PET FOOD ONLY,<br>NOT FOR HUMAN CONSUMPTION.<br>KEEP REFRIGERATED</div>
    <div class="flavour-band"><div class="flavour-title">ORIGINAL CHUNKY</div><div class="net-weight">Net weight:<b>1kg (35.27)</b></div></div>
    <div class="fortified-note">*with added vitamins, minerals and other nutrients</div>
  </article>

  <article class="label-unit">
    <div class="dog-photo" role="img" aria-label="Photo of a black, tan and white mountain dog, mouth open"></div>
    <div class="partner-mark">KUMUL<br>PETS</div>
    <div class="brand-lockup"><div class="brand-name">Brava Tusk</div><div class="brand-tagline">POWER FOR YOUR DOG</div></div>
    <div class="bone-tag"><svg viewBox="0 0 84 33"><use href="#bone-shape" fill="#111"/></svg><span>DOG FOOD</span></div>
    <div class="nutrition-claim">COMPLETE<br>NUTRITION<small>for all dogs big or small</small></div>
    <div class="storage-note">PET FOOD ONLY,<br>NOT FOR HUMAN CONSUMPTION.<br>KEEP REFRIGERATED</div>
    <div class="flavour-band"><div class="flavour-title">ORIGINAL CHUNKY</div><div class="net-weight">Net weight:<b>1kg (35.27)</b></div></div>
    <div class="fortified-note">*with added vitamins, minerals and other nutrients</div>
  </article>
</section>

</body>
</html>
```